Renaldo's Motorworks landing page to Dealership page, Rental Car Page, and Auto Body page.

I'm looking for my website to have RenaldosMotor.com be the landing page. From there visitors will have the option to visit three pages. My auto dealer page, of which I will provide an example of how I'd like it done. Auto body page, where I will fill in the text. The rental car page. Basically on the auto dealer and rental page I'll need the ability to add vehicles and delete as I need. Otherwise, its a pretty straightforward site. Nothing extensive. I already have the logo design from a previous project on here completed and can provide. If more funded needed for page capabilities, I can provide. I do have an account with HostPeak, with renaldosmotor.com already under them.

Target Market(s)

Automotive

Industry/Entity Type

Auto body repair, dealership, rental car.

Coding

Coded - Design and coding required

Number of Pages Required

4 page

Font styles to use
Sans Serif

Colors
0054AA
0677BA
7BADD7
CADEEF
E8F1F8

Requirements
Must have
• My logo Renaldos Motorworks at the top. Be creative with pics in the background of cars.
Nice to have
• Ease of use with being able to add vehicles for sale, and rental cars.
Should not have
• Nothing complex, would like to get in and out. Nothing to extensive on the designs of the pages, simple but attractive.

```html
<!DOCTYPE html>
<html lang="en">
<head>
<meta charset="utf-8">
<title>Renaldo's Motorworks – Car Rental</title>
<link href="https://fonts.googleapis.com/css2?family=Rubik:wght@300;400;500;700&display=swap" rel="stylesheet">
<style>
:root{
  --blue:#0677BA;
  --blue-dark:#0054AA;
  --blue-soft:#7BADD7;
  --blue-pale:#CADEEF;
  --blue-mist:#E8F1F8;
  --ink:#111;
  --text:#333;
  --muted:#777;
  --line:#e3e3e3;
  --band:#f7f7f7;
  --footer:#111;
}
*{box-sizing:border-box;margin:0;padding:0}
html,body{width:1200px;height:2773px;overflow:hidden}
body{font-family:'Rubik',sans-serif;color:var(--text);background:#fff;position:relative}
a{text-decoration:none;color:inherit}

/* header */
.site-header{position:absolute;top:0;left:0;width:1200px;height:101px}
.brand{position:absolute;left:161px;top:40px;display:flex;align-items:center;gap:8px;font-weight:700;font-size:18px;color:var(--ink)}
.brand-dot{width:16px;height:16px;border-radius:50%;background:var(--blue)}
.main-nav{position:absolute;left:412px;top:53px;display:flex;gap:17px;font-size:13px;color:#222}
.phone-btn{position:absolute;left:861px;top:35px;width:182px;height:46px;background:var(--blue);color:#fff;display:flex;align-items:center;justify-content:center;gap:12px;font-weight:500;font-size:15px}
.phone-rule{position:absolute;top:58px;height:1px;background:var(--blue)}

/* hero */
.hero{position:absolute;top:101px;left:0;width:1200px;height:525px;background:linear-gradient(180deg,#c7cde6 0%,#b9c3d9 35%,#6d8a55 55%,#5c6e4a 70%,#8a8a88 85%,#6b6b6a 100%)}
.hero-car{position:absolute;left:80px;top:205px;width:600px;height:270px;border-radius:120px 160px 40px 40px;background:linear-gradient(180deg,#4b4d52,#2a2b2e)}
.hero-copy{position:absolute;left:158px;top:58px;color:var(--ink)}
.hero-copy h1{font-size:35px;font-weight:700;line-height:39px;letter-spacing:.3px}
.hero-copy p{font-size:13px;line-height:24px;margin-top:18px;color:#111}
.hero-copy p span{color:var(--blue)}
.booking{position:absolute;left:762px;top:55px;width:285px;height:420px;background:#fff;padding:28px 20px 0 21px}
.field{height:44px;border:1px solid var(--line);display:flex;align-items:center;font-size:12.5px;color:#aaa;padding-left:12px;gap:12px}
.split{display:flex;margin-top:18px}
.split .tag{background:var(--blue);color:#fff;height:44px;display:flex;align-items:center;gap:10px;padding:0 12px;font-size:13px;width:98px}
.split .rest{flex:1;border:1px solid var(--line);border-left:none;height:44px;display:flex;align-items:center;padding-left:12px;gap:10px;font-size:12.5px;color:#aaa}
.hint{font-size:10.5px;color:#999;margin-top:12px}
.label{font-size:11px;color:#111;margin-top:22px}
.label + .split{margin-top:6px}
.book-btn{margin-top:28px;height:44px;background:var(--blue);color:#fff;font-weight:500;font-size:14px;display:flex;align-items:center;justify-content:center;position:relative}
.book-btn::before,.book-btn::after{content:"";position:absolute;top:22px;width:24px;height:1px;background:var(--blue)}
.book-btn::before{left:-24px}.book-btn::after{right:-24px}

/* deals */
.section-title{position:absolute;top:664px;left:0;width:1200px;display:flex;justify-content:center;align-items:center;gap:20px;font-size:24px;font-weight:700;color:var(--ink)}
.section-title i{width:24px;height:1px;background:var(--blue)}
.tabs{position:absolute;top:730px;left:0;width:1200px;display:flex;justify-content:center;gap:28px;font-size:12.5px;color:#666}
.tabs .active{color:var(--blue);font-weight:500;border-bottom:2px solid var(--blue);padding-bottom:6px}
.card{position:absolute;width:281px}
.card-photo{height:172px;position:relative}
.price{position:absolute;left:0;bottom:0;background:#fff;width:132px;height:34px;display:flex;align-items:center;padding-left:8px;font-size:13px;color:var(--blue)}
.card h3{font-size:14.5px;font-weight:500;color:#111;margin-top:17px}
.specs{display:flex;gap:18px;margin-top:17px;font-size:13px;color:#444}
.specs span{display:flex;align-items:center;gap:8px}
.card p{font-size:12.5px;line-height:19px;color:#888;margin-top:17px;padding-left:2px}
.rent-btn{margin-top:19px;margin-left:2px;width:115px;height:37px;border-radius:19px;background:var(--blue);color:#fff;font-size:13px;display:flex;align-items:center;justify-content:center}

/* steps */
.how{position:absolute;top:1610px;left:0;width:1200px;height:502px;background:var(--band);text-align:center}
.eyebrow{font-size:12px;color:var(--blue);letter-spacing:.3px}
.how .eyebrow{margin-top:50px}
.how h2{font-size:19px;font-weight:700;color:#111;margin-top:15px}
.how .lead{font-size:12.5px;line-height:19px;color:#777;margin:17px auto 0;width:440px}
.wave{position:absolute;left:0;top:165px}
.step{position:absolute;top:214px;width:240px;text-align:center}
.step-icon{width:76px;height:76px;border-radius:50%;background:#fff;margin:0 auto;position:relative;display:flex;align-items:center;justify-content:center;box-shadow:0 4px 14px rgba(0,0,0,.05)}
.step-num{position:absolute;top:-10px;right:6px;width:22px;height:22px;border-radius:50%;background:var(--blue);color:#fff;font-size:11px;display:flex;align-items:center;justify-content:center}
.step h4{font-size:16px;font-weight:500;color:#111;margin-top:24px}
.step p{font-size:12.5px;line-height:19px;color:#777;margin-top:13px}
.step a{display:inline-flex;gap:8px;align-items:center;font-size:12.5px;color:var(--blue);margin-top:23px}

/* testimonials */
.testi-intro{position:absolute;left:156px;top:2198px;width:330px}
.testi-intro .eyebrow{font-size:11px;color:var(--blue)}
.testi-intro h2{font-size:23px;font-weight:700;color:#111;margin-top:12px}
.testi-intro .sub{font-size:12.5px;color:#666;margin-top:17px}
.arrows{display:flex;gap:20px;margin-top:28px}
.arrows span{width:41px;height:41px;border-radius:50%;background:#f4f4f4;display:flex;align-items:center;justify-content:center}
.quote{position:absolute;top:2187px;width:304px;height:166px;border:2px solid #f1f1f1;border-radius:12px;padding:18px 24px 0 33px}
.quote p{font-size:12px;line-height:24px;color:#666}
.who{display:flex;align-items:center;gap:14px;margin-top:10px}
.avatar{width:42px;height:42px;border-radius:50%;background:linear-gradient(135deg,#c9b6a8,#6f5f57)}
.who b{display:block;font-size:13px;font-weight:500;color:#111}
.who small{font-size:12px;color:#aaa}
.who svg{margin-left:auto;margin-right:10px}

/* footer */
.site-footer{position:absolute;top:2405px;left:0;width:1200px;height:368px;background:var(--footer);color:#fff}
.f-brand{position:absolute;left:158px;top:100px;display:flex;align-items:center;gap:8px;font-weight:700;font-size:17px}
.f-brand .brand-dot{background:#fff}
.f-about{position:absolute;left:156px;top:160px;width:200px;font-size:11px;line-height:18px;color:#ddd}
.f-col{position:absolute;top:65px}
.f-col h5{font-size:16px;font-weight:500}
.f-col ul{list-style:none;margin-top:22px}
.addr li{display:flex;align-items:center;gap:14px;font-size:13px;height:45px}
.links li{font-size:13px;height:32px;padding-left:4px}
.social{display:flex;gap:9px;margin-top:24px}
.social span{width:25px;height:25px;border:1.5px solid #fff;border-radius:50%}
.copy{position:absolute;left:0;top:327px;width:1200px;text-align:center;font-size:11px;color:#ddd}
</style>
</head>
<body>

<header class="site-header">
  <a class="brand" href="#"><span class="brand-dot"></span>Renaldo's Motorworks</a>
  <nav class="main-nav">
    <a href="#">HOME</a><a href="#">DEALERSHIP</a><a href="#">CAR RENTAL</a><a href="#">AUTO BODY</a><a href="#">CONTACT US</a>
  </nav>
  <span class="phone-rule" style="left:843px;width:18px"></span>
  <span class="phone-rule" style="left:1043px;width:20px"></span>
  <a class="phone-btn" href="#">
    <svg width="20" height="20" viewBox="0 0 24 24" fill="none" stroke="#fff" stroke-width="1.6"><path d="M5 3h4l2 5-2.5 1.5a11 11 0 0 0 6 6L16 13l5 2v4a2 2 0 0 1-2 2A16 16 0 0 1 3 5a2 2 0 0 1 2-2z"/></svg>
    (555) 310-7724
  </a>
</header>

<section class="hero">
  <div class="hero-car" role="img" aria-label="Dark grey sports coupe parked on a country road"></div>
  <div class="hero-copy">
    <h1>RENT A CLASSY CAR<br>AT A LOW PRICE</h1>
    <p>Luxury Cars at low-cost, starts <span>$75 / day</span> from over<br>100 premium locations</p>
  </div>
  <form class="booking">
    <div class="field">
      <svg width="18" height="14" viewBox="0 0 24 18" fill="none" stroke="#aaa" stroke-width="1.4"><path d="M3 10l2-6h14l2 6v5H3z M3 10h18"/><circle cx="7" cy="13" r="1"/><circle cx="17" cy="13" r="1"/></svg>
      Select your car type<span style="margin-left:auto;margin-right:14px;font-size:9px">⌄</span>
    </div>
    <div class="split">
      <div class="tag"><svg width="14" height="16" viewBox="0 0 24 24" fill="none" stroke="#fff" stroke-width="2"><path d="M12 22s7-7 7-12a7 7 0 0 0-14 0c0 5 7 12 7 12z"/><circle cx="12" cy="10" r="2.5"/></svg>Pick up</div>
      <div class="rest">Enter your location</div>
    </div>
    <div class="hint">Need a different drop-off location?</div>
    <div class="label">Pick - up Date &amp; Time</div>
    <div class="split">
      <div class="tag" style="width:122px"><svg width="16" height="16" viewBox="0 0 24 24" fill="none" stroke="#fff" stroke-width="1.6"><rect x="3" y="5" width="18" height="16" rx="2"/><path d="M3 10h18M8 3v4M16 3v4"/></svg>04/10/2021</div>
      <div class="rest"><svg width="16" height="16" viewBox="0 0 24 24" fill="none" stroke="#aaa" stroke-width="1.5"><circle cx="12" cy="12" r="9"/><path d="M12 7v5l3 2"/></svg>12.00 am</div>
    </div>
    <div class="label">Drop - off Date &amp; Time</div>
    <div class="split">
      <div class="tag" style="width:122px"><svg width="16" height="16" viewBox="0 0 24 24" fill="none" stroke="#fff" stroke-width="1.6"><rect x="3" y="5" width="18" height="16" rx="2"/><path d="M3 10h18M8 3v4M16 3v4"/></svg>04/10/2021</div>
      <div class="rest"><svg width="16" height="16" viewBox="0 0 24 24" fill="none" stroke="#aaa" stroke-width="1.5"><circle cx="12" cy="12" r="9"/><path d="M12 7v5l3 2"/></svg>12.00 am</div>
    </div>
    <div class="book-btn">BOOK YOUR CAR NOW</div>
  </form>
</section>

<h2 class="section-title"><i></i>MOST POPULAR CAR RENTAL DEALS<i></i></h2>
<nav class="tabs">
  <span class="active">ALL</span><span>ARVEN</span><span>BRASK</span><span>KOVA</span><span>LUMEN</span><span>VELTRA</span><span>MERIDAN</span><span>PALLAS</span><span>TORVA</span>
</nav>

<!-- row 1 -->
<article class="card" style="left:154px;top:790px">
  <div class="card-photo" role="img" aria-label="Red compact SUV parked on a city street" style="background:linear-gradient(160deg,#5a4a42,#8a2b2e 55%,#4a4a4a)"><span class="price">$ 300.0 &nbsp;per day</span></div>
  <h3>VELTRA GT-8 SPORTS CAR</h3>
  <div class="specs"><span><svg width="20" height="14" viewBox="0 0 26 16" fill="none" stroke="#7BADD7" stroke-width="1.3"><circle cx="7" cy="5" r="3"/><circle cx="19" cy="5" r="3"/><circle cx="13" cy="6" r="3"/><path d="M1 15c0-4 3-6 6-6M25 15c0-4-3-6-6-6M7 15c0-4 3-6 6-6s6 2 6 6"/></svg>4 Person</span><span><svg width="20" height="14" viewBox="0 0 24 18" fill="none" stroke="#7BADD7" stroke-width="1.3"><path d="M3 10l2-6h14l2 6v5H3z M3 10h18"/></svg>Auto</span><span><svg width="16" height="16" viewBox="0 0 24 24" fill="none" stroke="#7BADD7" stroke-width="1.3"><rect x="4" y="3" width="12" height="18"/><path d="M7 7h6v4H7zM16 9l4 3v6"/></svg>Petrol</span></div>
  <p>Our coupe has broken tradition by ditching its torque converter automatic gearbox for</p>
  <a class="rent-btn" href="#">Rent Now</a>
</article>
<article class="card" style="left:459px;top:790px">
  <div class="card-photo" role="img" aria-label="Blue sports car on a racetrack" style="background:linear-gradient(180deg,#b8a890,#5d6470 45%,#1f3f8a 70%,#a89d8a)"><span class="price">$ 300.0 &nbsp;per day</span></div>
  <h3>VELTRA GT-8 SPORTS CAR</h3>
  <div class="specs"><span><svg width="20" height="14" viewBox="0 0 26 16" fill="none" stroke="#7BADD7" stroke-width="1.3"><circle cx="7" cy="5" r="3"/><circle cx="19" cy="5" r="3"/><circle cx="13" cy="6" r="3"/><path d="M1 15c0-4 3-6 6-6M25 15c0-4-3-6-6-6M7 15c0-4 3-6 6-6s6 2 6 6"/></svg>4 Person</span><span><svg width="20" height="14" viewBox="0 0 24 18" fill="none" stroke="#7BADD7" stroke-width="1.3"><path d="M3 10l2-6h14l2 6v5H3z M3 10h18"/></svg>Auto</span><span><svg width="16" height="16" viewBox="0 0 24 24" fill="none" stroke="#7BADD7" stroke-width="1.3"><rect x="4" y="3" width="12" height="18"/><path d="M7 7h6v4H7zM16 9l4 3v6"/></svg>Petrol</span></div>
  <p>Our coupe has broken tradition by ditching its torque converter automatic gearbox for</p>
  <a class="rent-btn" href="#">Rent Now</a>
</article>
<article class="card" style="left:764px;top:790px">
  <div class="card-photo" role="img" aria-label="Red sedan parked by the sea" style="background:linear-gradient(180deg,#c6d8e6,#8fb2c4 40%,#a01f34 65%,#8a8a8a)"><span class="price">$ 300.0 &nbsp;per day</span></div>
  <h3>VELTRA GT-8 SPORTS CAR</h3>
  <div class="specs"><span><svg width="20" height="14" viewBox="0 0 26 16" fill="none" stroke="#7BADD7" stroke-width="1.3"><circle cx="7" cy="5" r="3"/><circle cx="19" cy="5" r="3"/><circle cx="13" cy="6" r="3"/><path d="M1 15c0-4 3-6 6-6M25 15c0-4-3-6-6-6M7 15c0-4 3-6 6-6s6 2 6 6"/></svg>4 Person</span><span><svg width="20" height="14" viewBox="0 0 24 18" fill="none" stroke="#7BADD7" stroke-width="1.3"><path d="M3 10l2-6h14l2 6v5H3z M3 10h18"/></svg>Auto</span><span><svg width="16" height="16" viewBox="0 0 24 24" fill="none" stroke="#7BADD7" stroke-width="1.3"><rect x="4" y="3" width="12" height="18"/><path d="M7 7h6v4H7zM16 9l4 3v6"/></svg>Petrol</span></div>
  <p>Our coupe has broken tradition by ditching its torque converter automatic gearbox for</p>
  <a class="rent-btn" href="#">Rent Now</a>
</article>

<!-- row 2 -->
<article class="card" style="left:154px;top:1187px">
  <div class="card-photo" role="img" aria-label="Silver sports coupe at sunset" style="background:linear-gradient(180deg,#9a8e8a,#c9a58e 40%,#a7a9ad 65%,#4d4d4f)"><span class="price">$ 300.0 &nbsp;per day</span></div>
  <h3>VELTRA GT-8 SPORTS CAR</h3>
  <div class="specs"><span><svg width="20" height="14" viewBox="0 0 26 16" fill="none" stroke="#7BADD7" stroke-width="1.3"><circle cx="7" cy="5" r="3"/><circle cx="19" cy="5" r="3"/><circle cx="13" cy="6" r="3"/><path d="M1 15c0-4 3-6 6-6M25 15c0-4-3-6-6-6M7 15c0-4 3-6 6-6s6 2 6 6"/></svg>4 Person</span><span><svg width="20" height="14" viewBox="0 0 24 18" fill="none" stroke="#7BADD7" stroke-width="1.3"><path d="M3 10l2-6h14l2 6v5H3z M3 10h18"/></svg>Auto</span><span><svg width="16" height="16" viewBox="0 0 24 24" fill="none" stroke="#7BADD7" stroke-width="1.3"><rect x="4" y="3" width="12" height="18"/><path d="M7 7h6v4H7zM16 9l4 3v6"/></svg>Petrol</span></div>
  <p>Our coupe has broken tradition by ditching its torque converter automatic gearbox for</p>
  <a class="rent-btn" href="#">Rent Now</a>
</article>
<article class="card" style="left:459px;top:1187px">
  <div class="card-photo" role="img" aria-label="White sport sedan in front of a grey wall" style="background:linear-gradient(180deg,#8f9499,#c8cbce 45%,#e9e9ea 65%,#6d6a66)"><span class="price">$ 300.0 &nbsp;per day</span></div>
  <h3>VELTRA GT-8 SPORTS CAR</h3>
  <div class="specs"><span><svg width="20" height="14" viewBox="0 0 26 16" fill="none" stroke="#7BADD7" stroke-width="1.3"><circle cx="7" cy="5" r="3"/><circle cx="19" cy="5" r="3"/><circle cx="13" cy="6" r="3"/><path d="M1 15c0-4 3-6 6-6M25 15c0-4-3-6-6-6M7 15c0-4 3-6 6-6s6 2 6 6"/></svg>4 Person</span><span><svg width="20" height="14" viewBox="0 0 24 18" fill="none" stroke="#7BADD7" stroke-width="1.3"><path d="M3 10l2-6h14l2 6v5H3z M3 10h18"/></svg>Auto</span><span><svg width="16" height="16" viewBox="0 0 24 24" fill="none" stroke="#7BADD7" stroke-width="1.3"><rect x="4" y="3" width="12" height="18"/><path d="M7 7h6v4H7zM16 9l4 3v6"/></svg>Petrol</span></div>
  <p>Our coupe has broken tradition by ditching its torque converter automatic gearbox for</p>
  <a class="rent-btn" href="#">Rent Now</a>
</article>
<article class="card" style="left:764px;top:1187px">
  <div class="card-photo" role="img" aria-label="Dark SUV in front of mountains" style="background:linear-gradient(180deg,#a9b3b9,#6f7a6c 40%,#3d3f47 70%,#8b8780)"><span class="price">$ 300.0 &nbsp;per day</span></div>
  <h3>VELTRA GT-8 SPORTS CAR</h3>
  <div class="specs"><span><svg width="20" height="14" viewBox="0 0 26 16" fill="none" stroke="#7BADD7" stroke-width="1.3"><circle cx="7" cy="5" r="3"/><circle cx="19" cy="5" r="3"/><circle cx="13" cy="6" r="3"/><path d="M1 15c0-4 3-6 6-6M25 15c0-4-3-6-6-6M7 15c0-4 3-6 6-6s6 2 6 6"/></svg>4 Person</span><span><svg width="20" height="14" viewBox="0 0 24 18" fill="none" stroke="#7BADD7" stroke-width="1.3"><path d="M3 10l2-6h14l2 6v5H3z M3 10h18"/></svg>Auto</span><span><svg width="16" height="16" viewBox="0 0 24 24" fill="none" stroke="#7BADD7" stroke-width="1.3"><rect x="4" y="3" width="12" height="18"/><path d="M7 7h6v4H7zM16 9l4 3v6"/></svg>Petrol</span></div>
  <p>Our coupe has broken tradition by ditching its torque converter automatic gearbox for</p>
  <a class="rent-btn" href="#">Rent Now</a>
</article>

<section class="how">
  <p class="eyebrow">HOW IT WORKS</p>
  <h2>3 Easy Step For Rent Our Car</h2>
  <p class="lead">Lorem ipsum dolor sit amet, consectetur adipiscing elit. Ut elit tellus, luctus nec ullamcorper mattis, pulvinar dapibus leo.</p>
  <svg class="wave" width="1200" height="160" viewBox="0 0 1200 160" fill="none" stroke="#cfcfcf" stroke-width="1.2" stroke-dasharray="6 6"><path d="M0 80C80 20 130 40 180 100S290 110 340 60 430 -10 490 60 560 150 620 110 700 20 770 50 820 140 880 120 960 20 1040 40 1110 150 1200 90"/></svg>
  <div class="step" style="left:170px">
    <div class="step-icon"><span class="step-num">1</span><svg width="44" height="26" viewBox="0 0 44 26" fill="none" stroke="#0677BA" stroke-width="1.6"><path d="M3 18v-5l6-2 6-6h14l8 6 4 1v6z"/><circle cx="12" cy="19" r="3.5" fill="#fff"/><circle cx="33" cy="19" r="3.5" fill="#fff"/></svg></div>
    <h4>Choose a Car</h4>
    <p>Lorem ipsum dolor sit amet, consect<br>etur adipiscing elit.</p>
    <a href="#">Car List <svg width="14" height="10" viewBox="0 0 14 10" fill="none" stroke="#0677BA" stroke-width="1.3"><path d="M0 5h13M9 1l4 4-4 4"/></svg></a>
  </div>
  <div class="step" style="left:476px">
    <div class="step-icon"><span class="step-num">2</span><svg width="36" height="36" viewBox="0 0 36 36" fill="none" stroke="#0677BA" stroke-width="1.6"><rect x="3" y="6" width="24" height="22" rx="2"/><path d="M3 12h24M9 3v6M21 3v6"/><circle cx="27" cy="27" r="7" fill="#fff"/><path d="M24 27l2 2 4-4"/></svg></div>
    <h4>Book a Date</h4>
    <p>Lorem ipsum dolor sit amet, consect<br>etur adipiscing elit.</p>
    <a href="#">Select Date <svg width="14" height="10" viewBox="0 0 14 10" fill="none" stroke="#0677BA" stroke-width="1.3"><path d="M0 5h13M9 1l4 4-4 4"/></svg></a>
  </div>
  <div class="step" style="left:782px">
    <div class="step-icon"><span class="step-num">3</span><svg width="32" height="32" viewBox="0 0 32 32" fill="none" stroke="#0677BA" stroke-width="1.6"><circle cx="16" cy="16" r="13"/><path d="M10 16l4 4 8-8"/></svg></div>
    <h4>Enjoy the Car</h4>
    <p>Lorem ipsum dolor sit amet, consect<br>etur adipiscing elit.</p>
    <a href="#">Review Us <svg width="14" height="10" viewBox="0 0 14 10" fill="none" stroke="#0677BA" stroke-width="1.3"><path d="M0 5h13M9 1l4 4-4 4"/></svg></a>
  </div>
</section>

<section>
  <div class="testi-intro">
    <p class="eyebrow">TESTIMONIALS</p>
    <h2>What Clients Say About Us</h2>
    <p class="sub">Lorem ipsum dolor sit amet, consectetur adipiscing elit.</p>
    <div class="arrows">
      <span><svg width="16" height="10" viewBox="0 0 16 10" fill="none" stroke="#aaa" stroke-width="1.2"><path d="M16 5H1M5 1L1 5l4 4"/></svg></span>
      <span><svg width="16" height="10" viewBox="0 0 16 10" fill="none" stroke="#aaa" stroke-width="1.2"><path d="M0 5h15M11 1l4 4-4 4"/></svg></span>
    </div>
  </div>
  <blockquote class="quote" style="left:537px">
    <p>Lorem ipsum dolor sit amet, consectetur adipiscing elit. Ut elit tellus, luctus nec ullamcorper mattis, pulvinar</p>
    <div class="who"><span class="avatar" role="img" aria-label="Client portrait"></span><div><b>Lena Marsh</b><small>client</small></div><svg width="30" height="20" viewBox="0 0 30 20" fill="#0677BA"><path d="M2 18c6-2 9-6 9-12V2H4v7h3c0 4-2 7-5 9zM17 18c6-2 9-6 9-12V2h-7v7h3c0 4-2 7-5 9z"/></svg></div>
  </blockquote>
  <blockquote class="quote" style="left:867px">
    <p>Lorem ipsum dolor sit amet, consectetur adipiscing elit. Ut elit tellus, luctus nec ullamcorper mattis, pulvinar</p>
    <div class="who"><span class="avatar" role="img" aria-label="Client portrait" style="background:linear-gradient(135deg,#b7b7b7,#4a4a4a)"></span><div><b>Owen Ridley</b><small>client</small></div><svg width="30" height="20" viewBox="0 0 30 20" fill="#0677BA"><path d="M2 18c6-2 9-6 9-12V2H4v7h3c0 4-2 7-5 9zM17 18c6-2 9-6 9-12V2h-7v7h3c0 4-2 7-5 9z"/></svg></div>
  </blockquote>
</section>

<footer class="site-footer">
  <div class="f-brand"><span class="brand-dot"></span>Renaldo's Motorworks</div>
  <p class="f-about">Lorem ipsum dolor sit amet, consecte-tur adipiscing elit. Quisque pharetra condimentum.</p>
  <div class="f-col addr" style="left:412px">
    <h5>Our Address</h5>
    <ul>
      <li><svg width="16" height="16" viewBox="0 0 24 24" fill="none" stroke="#fff" stroke-width="1.5"><path d="M12 22s7-7 7-12a7 7 0 0 0-14 0c0 5 7 12 7 12z"/><circle cx="12" cy="10" r="2.5"/></svg>418 Harlow Ave, Brookfield</li>
      <li><svg width="16" height="16" viewBox="0 0 24 24" fill="none" stroke="#fff" stroke-width="1.5"><path d="M5 3h4l2 5-2.5 1.5a11 11 0 0 0 6 6L16 13l5 2v4a2 2 0 0 1-2 2A16 16 0 0 1 3 5a2 2 0 0 1 2-2z"/></svg>+1 555 208 1147</li>
      <li><svg width="16" height="14" viewBox="0 0 24 18" fill="none" stroke="#fff" stroke-width="1.5"><rect x="2" y="2" width="20" height="14"/><path d="M2 2l10 8 10-8"/></svg>hello@renaldosmotor.com</li>
      <li><svg width="16" height="16" viewBox="0 0 24 24" fill="none" stroke="#fff" stroke-width="1.5"><circle cx="12" cy="12" r="9"/><path d="M12 7v5l3 2"/></svg>09.00 - 17.00</li>
    </ul>
  </div>
  <div class="f-col links" style="left:659px">
    <h5>Quick Links</h5>
    <ul><li>Home</li><li>Dealership</li><li>Car Rental</li><li>Auto Body</li><li>Contact us</li></ul>
  </div>
  <div class="f-col" style="left:871px">
    <h5>Follow Us</h5>
    <div class="social"><span></span><span></span><span></span><span></span></div>
  </div>
  <p class="copy">Copyright © 2021 RenaldosMotor.com.</p>
</footer>

</body>
</html>
```